Vocational Mentor needs an impressive business card

1. I need a business card (or maybe three with identic look) to promote me and my three business titles/services:
- Vocational Mentor. I help people find their vocation and live happily from it. I use my 20 years of experience in business, management and psychology to help them identify the most efficient ways to make a living doing what they are passionate about.
- Business Angel. I help founders start a succesful business with minimum risks and costs. I use my 20 years of experience in sales, management and entrepreneurship to help them identify the most efficient ways, in terms of time and cost, to validate their business idea.
- Learning Designer. I design unique learning programs that produce long-term cognitive and behavioural changes to people and organisations. I use my 20 years of experience in learning, teaching and change management to create minimalist experiences and processes that allow them to change efficiently in their pursued direction.

2. I would like a two-sided business card, on the front with my name, contact details and titles, on the back the explanation of the services.
Updates

Hi all,

I updated my brief, included contacts info and give feedback on all designs I got. I am new on this platform so please tell me if you need anything else or if I don't use corectly the platform forms.

Kind regards,
Tudor

Hi all,

I shortened the services description by deleting the phrase "I call..."

Kind regards,
Tudor

Target Market(s)

Freelancers, startups, people and organization willing to invest in change through ultimate learning experiences

Industry/Entity Type

Business

Font styles to use
Serif

Requirements
Must have
• Front side: full name, titles, web site, email, phone like below:
Tudor Vasilache
Vocational Mentor, Business Angel, Learning Designer
info@tudorvasilache.example
www.tudorvasilache.example
+40-745-TUDORV
Nice to have
• Back side: the description of the services I provide as in the task description.
1/3: it would be nice if I can jam all three titles on the front side but then I need a solution to jam all three services on the back side.

```html
<!DOCTYPE html>
<html lang="en">
<head>
<meta charset="utf-8">
<title>Tudor Vasilache – Business Cards</title>
<link href="https://fonts.googleapis.com/css2?family=Open+Sans:wght@400;700&display=swap" rel="stylesheet">
<style>
  :root {
    --page-bg: #2b2b2c;
    --card-top: #3b3b3d;
    --card-bottom: #1f1f20;
    --accent-band: #5d5d60;
    --accent-band-light: #6a6a6d;
    --name-color: #f4f4f4;
    --text-color: #dcdcdc;
  }
  html, body {
    margin: 0;
    width: 1200px;
    height: 900px;
    overflow: hidden;
    background: var(--page-bg);
    font-family: "Open Sans", Arial, sans-serif;
  }
  .business-card {
    position: absolute;
    left: 250px;
    width: 700px;
    height: 400px;
    background: linear-gradient(165deg, var(--card-top) 0%, var(--card-bottom) 100%);
    box-shadow: 0 14px 32px rgba(0,0,0,0.45);
    overflow: hidden;
  }
  .card-back { top: 40px; }
  .card-front { top: 470px; }
  .card-bands {
    position: absolute;
    inset: 0;
  }
  .holder-name {
    position: absolute;
    left: 52px;
    margin: 0;
    font-size: 34px;
    font-weight: 700;
    line-height: 44px;
    color: var(--name-color);
    letter-spacing: 0.4px;
  }
  .holder-titles {
    position: absolute;
    left: 55px;
    margin: 0;
    font-size: 16px;
    line-height: 22px;
    color: var(--text-color);
  }
  .card-back .holder-name { top: 100px; }
  .card-back .holder-titles { top: 162px; }
  .card-front .holder-name { top: 76px; }
  .card-front .holder-titles { top: 146px; }
  .holder-phone {
    position: absolute;
    left: 55px;
    top: 194px;
    margin: 0;
    font-size: 16px;
    line-height: 22px;
    color: var(--text-color);
    display: flex;
    align-items: center;
    gap: 7px;
  }
  .contact-online {
    position: absolute;
    left: 400px;
    top: 294px;
    margin: 0;
    font-size: 16px;
    line-height: 25px;
    color: var(--text-color);
  }
  .contact-online span { display: block; }
</style>
</head>
<body>
  <section class="business-card card-back">
    <svg class="card-bands" width="700" height="400" viewBox="0 0 700 400" aria-hidden="true">
      <polygon points="0,262 430,262 462,400 440,400 414,276 0,276" fill="var(--accent-band)"/>
    </svg>
    <h2 class="holder-name">Tudor Vasilache</h2>
    <p class="holder-titles">Vocational Mentor, Business Angel,<br>Learning Designer</p>
  </section>

  <section class="business-card card-front">
    <svg class="card-bands" width="700" height="400" viewBox="0 0 700 400" aria-hidden="true">
      <polygon points="0,254 282,254 310,400 285,400 261,268 0,268" fill="var(--accent-band)"/>
      <polygon points="320,274 342,274 369,362 700,362 700,385 352,385" fill="var(--accent-band-light)"/>
    </svg>
    <h1 class="holder-name">Tudor Vasilache</h1>
    <p class="holder-titles">Vocational Mentor, Business Angel,<br>Learning Designer</p>
    <p class="holder-phone">
      <svg width="10" height="16" viewBox="0 0 12 20" aria-hidden="true">
        <rect x="1" y="1" width="10" height="18" rx="2" fill="none" stroke="var(--text-color)" stroke-width="1.5"/>
        <rect x="3" y="4" width="6" height="8" fill="var(--text-color)"/>
      </svg>
      +40-745-TUDORV
    </p>
    <p class="contact-online">
      <span>@ info@tudorvasilache.example</span>
      <span>www.tudorvasilache.example</span>
    </p>
  </section>
</body>
</html>
```